Brookfell Self Storage - Business Sign

The sign we are needing designed is our main road sign for our self-storage business. The dimensions of the sign are 57 inches tall x 96 inches wide. We require that our attached logo be on the sign as well as our phone number: 478-216-4387 and website www.BrookfellStorage.net. Optional information that can be added but not required is our address: 418 Marlow Tenney Pkwy, Centerville, GA 31047.

Industry/Entity Type

Self Storage

Font styles to use
Sans Serif

```html
<!DOCTYPE html>
<html lang="en">
<head>
<meta charset="utf-8">
<title>Brookfell Self Storage – Road Sign</title>
<link href="https://fonts.googleapis.com/css2?family=Arimo:wght@700&family=Open+Sans:wght@700&display=swap" rel="stylesheet">
<style>
  :root {
    --page-bg: #f3f3f3;
    --sign-white: #ffffff;
    --brand-navy: #035db7;
    --brand-sky: #4baefd;
    --phone-shadow: #3a82d1;
    --logo-grey: #454545;
    --text-white: #ffffff;
  }
  * { margin: 0; padding: 0; box-sizing: border-box; }
  html, body {
    width: 1200px;
    height: 851px;
    overflow: hidden;
    background: var(--page-bg);
  }
  .sign {
    position: absolute;
    left: 40px;
    top: 93px;
    width: 1120px;
    height: 665px;
    background: var(--sign-white);
    display: flex;
    flex-direction: column;
  }
  .sign__brand {
    height: 366px;
    display: flex;
    align-items: center;
    justify-content: center;
    gap: 24px;
  }
  .brand-mark {
    width: 46px;
    height: 46px;
    background: var(--brand-navy);
  }
  .brand-name {
    font-family: "Open Sans", sans-serif;
    font-weight: 700;
    font-size: 62px;
    color: var(--logo-grey);
    letter-spacing: 1px;
  }
  .band { width: 100%; }
  .band--top { height: 61px; background: var(--brand-navy); }
  .band--phone {
    height: 135px;
    background: var(--brand-sky);
    display: flex;
    align-items: center;
    justify-content: center;
  }
  .phone {
    font-family: "Arimo", sans-serif;
    font-weight: 700;
    font-size: 112px;
    line-height: 1;
    color: var(--text-white);
    letter-spacing: -1px;
    text-shadow: 6px 6px 0 var(--phone-shadow);
  }
  .band--web {
    height: 103px;
    background: var(--brand-navy);
    display: flex;
    align-items: center;
    justify-content: center;
  }
  .website {
    font-family: "Open Sans", sans-serif;
    font-weight: 700;
    font-size: 54px;
    line-height: 1;
    color: var(--text-white);
    letter-spacing: 2px;
  }
</style>
</head>
<body>
  <main class="sign">
    <header class="sign__brand">
      <span class="brand-mark" aria-hidden="true"></span>
      <h1 class="brand-name">Brookfell Self Storage</h1>
    </header>
    <div class="band band--top"></div>
    <div class="band band--phone">
      <p class="phone">478-216-4387</p>
    </div>
    <div class="band band--web">
      <p class="website">www.BrookfellStorage.net</p>
    </div>
  </main>
</body>
</html>
```